Pale Lanterns Old Lane Walk Poster Design

We need an A4 sized poster to promote our weekly true crime tours. This poster will be posted onto community noticeboards.
Lots of information and images can be viewed at the following links:-
www.palelanterns.com.au
www.palelanterns.com.au/bookings/
https://www.facebook.com/palelanternsoldlane/
https://www.examplereviews.com.au/Attraction_Review-g000000-d00000000-Reviews-Pale_Lanterns-Newcastle_Greater_Newcastle_New_South_Wales.html
There are also a number of images for possible use at the following link - we are open to intepretation:-
http://palelanterns.com.au/tour-photographs/
The font on our website is "SpecialElite" so we would like to continue using that font type.
Target Market(s)
Adults 25-65.
Font styles to use
Other font styles liked:
- Special Elite
Colors
Designer to choose colors to be used in the design.
Look and feel
Each slider illustrates characteristics of the customer's brand and the style your logo design should communicate.

```html
<!DOCTYPE html>
<html lang="en">
<head>
<meta charset="utf-8">
<title>Pale Lanterns Old Lane Walk Poster</title>
<link rel="stylesheet" href="https://fonts.googleapis.com/css2?family=Special+Elite&family=Open+Sans:wght@400;600&display=swap">
<style>
  :root {
    --backdrop: #a7a7a7;
    --poster-dark: #262626;
    --photo-light: #4a4a4a;
    --photo-mid: #303030;
    --photo-deep: #1c1c1c;
    --ink-white: #f3f3f3;
    --ink-red: #e3161d;
  }
  html, body {
    margin: 0;
    width: 1200px;
    height: 800px;
    overflow: hidden;
    background: var(--backdrop);
  }
  .poster {
    position: absolute;
    left: 338px;
    top: 30px;
    width: 524px;
    height: 740px;
    background: var(--poster-dark);
    overflow: hidden;
    font-family: "Special Elite", "Courier New", monospace;
    text-align: center;
  }
  .poster__photo {
    position: absolute;
    inset: 0;
    background:
      radial-gradient(ellipse 70% 45% at 50% 38%, var(--photo-light) 0%, var(--photo-mid) 55%, transparent 100%),
      linear-gradient(180deg, var(--photo-mid) 0%, var(--photo-deep) 55%, var(--photo-mid) 100%);
  }
  .poster__line {
    position: absolute;
    left: 0;
    right: 0;
    margin: 0;
    line-height: 1;
  }
  .brand {
    top: 144px;
    font-family: "Open Sans", Arial, sans-serif;
    font-weight: 600;
    font-size: 17px;
    color: var(--ink-red);
    letter-spacing: 0.5px;
  }
  .headline {
    font-size: 37px;
    letter-spacing: 0.5px;
  }
  .headline--white { color: var(--ink-white); }
  .headline--red { color: var(--ink-red); }
  .headline--1 { top: 275px; }
  .headline--2 { top: 322px; }
  .headline--3 { top: 369px; }
  .headline--4 { top: 416px; }
  .tagline {
    top: 557px;
    font-size: 19px;
    letter-spacing: 2px;
    color: var(--ink-red);
  }
  .subline {
    top: 589px;
    font-family: "Open Sans", Arial, sans-serif;
    font-size: 17px;
    color: var(--ink-red);
  }
  .event-date {
    top: 634px;
    font-size: 15px;
    color: var(--ink-white);
    line-height: 19px;
  }
  .event-date sup { font-size: 8px; }
  .booking {
    position: absolute;
    left: 136px;
    top: 688px;
    width: 249px;
    height: 30px;
    border: 2px solid var(--ink-red);
    color: var(--ink-red);
    font-size: 18px;
    line-height: 30px;
    letter-spacing: 1.5px;
    box-sizing: content-box;
  }
</style>
</head>
<body>
  <main class="poster">
    <div class="poster__photo" role="img" aria-label="Dark black-and-white photograph of an old tram on a rainy street at night"></div>

    <p class="poster__line brand">PALE LANTERNS</p>

    <h1 class="poster__line headline headline--white headline--1">TAKE A WALK ON</h1>
    <p class="poster__line headline headline--red headline--2">THE DARK SIDE</p>
    <p class="poster__line headline headline--white headline--3">REVISIT THE SCENES OF</p>
    <p class="poster__line headline headline--red headline--4">THE CRIMES.</p>

    <p class="poster__line tagline">100% TRUE - 100% UNBELIEVABLE</p>
    <p class="poster__line subline">......stories the city tried to forget.......</p>

    <p class="poster__line event-date">28<sup>th</sup> April,2018<br>10:00 AM</p>

    <div class="booking">BOOKINGS ESSENTIAL.</div>
  </main>
</body>
</html>
```